Design for new site

Hi, we need a web design for a new product calmridgeway.
This product is aimed to help people with anxiety, panic attacks and other disorders on permanently basis.
Please take a look at competitors web-sites:
http://www.brightharborpath.example/
http://www.stillmeadow.example/
Key Audiences
The intended audience for this site will be people that are looking for relief from panic and anxiety.
Key Objectives
Key object is to get prospective clients to sign up for membership and purchase our audio course.
Theme of Site
The general site theme needs to be clean and simple. The audience coming to the site in under a lot of anxiety and we don’t want to add any stress.
The site needs to flow easy from top down, with few distractions in side menus and/or columns.
Color Scheme
Suggested colors need to be light shades of blue. Blue psychology is tranquil, peaceful, and calm. This color has a tremendous stress management quality to it, making us feel cool and calm.
Or it can be shades of cool green of summer forest.
Please take a look at site mock up in attachment.

```html
<!DOCTYPE html>
<html lang="en">
<head>
<meta charset="utf-8">
<title>Calmridgeway – Relief from panic and anxiety</title>
<link rel="stylesheet" href="https://fonts.googleapis.com/css2?family=PT+Sans+Narrow:wght@400;700&family=Source+Sans+3:ital,wght@0,400;0,600;0,700;1,700&display=swap">
<style>
:root{
  --teal:#139dbf;
  --teal-pale:#cfe9f1;
  --navy:#0b2a5b;
  --navy-text:#12305f;
  --yellow:#e8b500;
  --grey-bg:#d4d4d4;
  --panel:#ffffff;
  --input:#cdd5de;
  --link:#3aa0d8;
  --report:#1c5fa8;
  --white:#ffffff;
}
*{box-sizing:border-box;margin:0;padding:0}
html,body{width:768px;height:1200px;overflow:hidden}
body{position:relative;background:var(--grey-bg);font-family:"Source Sans 3",Arial,sans-serif;color:var(--navy-text)}
.abs{position:absolute}
.narrow{font-family:"PT Sans Narrow","Arial Narrow",sans-serif}

.top-bar{left:0;top:0;width:768px;height:29px;background:var(--teal)}
.social{display:flex;gap:4px}
.social span{width:18px;height:18px;border-radius:50%;background:var(--white);display:block}
.top-bar .social{position:absolute;left:490px;top:6px}

.header{left:0;top:29px;width:768px;height:56px;background:var(--white);text-align:center}
.brand{font-family:"Source Sans 3",Arial,sans-serif;font-weight:700;color:var(--teal);letter-spacing:1px}
.header .brand{font-size:34px;line-height:56px}

.hero{left:0;top:85px;width:768px;height:251px;background:linear-gradient(90deg,#a9a4a2 0%,#c8c2bd 20%,#b9cfe0 45%,#d4dde5 60%,#bfb8b2 80%,#9e9893 100%)}
.hero-badge{left:160px;top:130px;width:144px;height:144px;border-radius:50%;background:var(--yellow);color:var(--navy-text);display:flex;align-items:center;justify-content:center;text-align:center;font-size:14.5px;line-height:19px;padding:8px}

.panel{left:142px;top:316px;width:485px;height:756px;background:var(--panel)}
.signup-tab{left:413px;top:291px;width:214px;height:25px;background:var(--teal);color:var(--white);font-family:"PT Sans Narrow","Arial Narrow",sans-serif;font-style:italic;font-weight:700;font-size:13px;line-height:25px;padding-left:35px}
.now-title{left:435px;top:317px;font-family:"PT Sans Narrow","Arial Narrow",sans-serif;font-style:italic;font-weight:700;font-size:19px;line-height:22px;color:var(--navy-text)}
.disc{left:568px;top:302px}

.video{left:156px;top:335px;width:236px;height:148px;background:var(--teal)}
.video svg{position:absolute;left:85px;top:41px}

.form-row{left:425px;display:flex;align-items:center}
.form-row label{width:36px;font-size:6.5px;font-weight:600;color:var(--navy-text)}
.form-row span{width:107px;height:15px;background:var(--input);border-radius:2px;display:block}
.privacy{left:460px;top:430px;font-size:5.5px;color:#6b7a8c}
.btn{background:var(--teal);color:var(--white);font-family:"PT Sans Narrow","Arial Narrow",sans-serif;font-style:italic;font-weight:700;border-radius:11px;text-align:center;white-space:nowrap}
.form-btn{left:459px;top:446px;width:112px;height:20px;font-size:11px;line-height:20px}
.form-arrow{left:400px;top:418px}

.section-title{font-size:19px;font-weight:400;color:var(--navy-text);text-align:center}
.relief-title{left:142px;top:491px;width:485px}

.feature{width:150px;text-align:center}
.feature .icon{width:50px;height:50px;border-radius:50%;background:var(--teal);margin:0 auto;display:flex;align-items:center;justify-content:center}
.feature h3{font-family:"PT Sans Narrow","Arial Narrow",sans-serif;font-weight:400;font-size:16px;margin-top:6px;color:var(--navy-text)}
.feature p{font-size:7.5px;line-height:9.5px;margin-top:3px;padding:0 14px}
.feature a{color:var(--link);text-decoration:none}
.feature ul{list-style:none;text-align:left;font-size:7.5px;line-height:12.5px;margin:4px 0 0 20px}
.feature li::before{content:"";display:inline-block;border-left:4px solid var(--navy-text);border-top:3px solid transparent;border-bottom:3px solid transparent;margin-right:7px}

.about{left:142px;top:673px;width:485px;height:162px;background:var(--teal);color:var(--white)}
.about h2{font-family:"PT Sans Narrow","Arial Narrow",sans-serif;font-weight:400;font-size:17px;text-align:center;margin-top:5px}
.about-image{left:15px;top:33px;width:147px;height:98px;background:#256e74;border:1.5px solid var(--white)}
.about-text{left:177px;top:34px;width:292px;font-size:7.3px;line-height:9.6px}
.about-text p+p{margin-top:9px}

.divider{left:394px;top:837px;width:1px;height:235px;background:#cfcfcf}
.col-title{font-family:"PT Sans Narrow","Arial Narrow",sans-serif;font-weight:400;font-size:17px;text-align:center;color:var(--navy-text)}
.pill{left:152px;width:234px;height:32px;border-radius:14px;font-size:7.2px;line-height:9px;padding:0 14px;display:flex;align-items:center}
.pill-teal{background:var(--teal);color:var(--white)}
.pill-pale{background:var(--teal-pale);color:var(--navy-text)}
.secret-report{left:164px;top:996px;width:220px;font-family:"PT Sans Narrow","Arial Narrow",sans-serif;font-size:9.6px;line-height:12.4px;color:var(--report)}
.read-more{font-family:"PT Sans Narrow","Arial Narrow",sans-serif;font-size:7.5px;color:var(--navy-text);text-decoration:none}

.avatar{width:60px;height:60px;border-radius:50%}
.quote{left:474px;width:140px;font-size:7.5px;line-height:9.6px}
.quote b{display:block;margin-top:6px;color:#3b78b5;font-weight:700}

.cta-bar{left:142px;top:1072px;width:485px;height:25px;background:var(--teal);color:var(--white);display:flex;align-items:center}
.cta-bar p{margin-left:106px;font-size:12.5px}
.cta-bar .btn{margin-left:15px;background:var(--white);color:var(--teal);font-size:9.5px;height:19px;line-height:19px;width:116px;border-radius:10px}

.footer{left:142px;top:1099px;width:485px;height:101px;background:var(--navy);color:var(--white)}
.footer .social{position:absolute;left:17px;top:31px;gap:3px}
.footer .social span{width:19px;height:19px}
.footer-links{left:19px;top:61px;font-size:7.5px;font-weight:700}
.footer .brand{position:absolute;left:306px;top:28px;font-size:16px;color:var(--yellow)}
.copyright{left:364px;top:60px;font-size:7.5px}
</style>
</head>
<body>

<div class="abs top-bar"><div class="social"><span></span><span></span><span></span><span></span><span></span><span></span></div></div>

<header class="abs header"><div class="brand">CALMRIDGEWAY</div></header>

<div class="abs hero" role="img" aria-label="Photo of an excited woman in glasses pulling open her shirt like a superhero against a blurred city sky"></div>
<div class="abs hero-badge narrow">Our aimed<br>to help people with<br>anxiety, panic attacks and<br>other disorders on<br>permanently basis.</div>

<main class="abs panel"></main>

<div class="abs signup-tab">Sign up for membership</div>
<div class="abs now-title">Calmridgeway NOW!</div>
<svg class="abs disc" width="48" height="48" viewBox="0 0 48 48" aria-hidden="true">
  <circle cx="26" cy="22" r="21" fill="var(--teal)"/>
  <path d="M26 1 A21 21 0 0 1 44 33 L26 22 Z" fill="var(--yellow)"/>
  <circle cx="26" cy="22" r="5" fill="#fff"/>
</svg>
<svg class="abs" style="left:548px;top:337px" width="24" height="14" viewBox="0 0 24 14" aria-hidden="true">
  <path d="M1 4 Q10 12 20 6" stroke="var(--yellow)" stroke-width="2" fill="none"/>
  <path d="M16 3 L21 6 L17 10" stroke="var(--yellow)" stroke-width="2" fill="none"/>
</svg>

<div class="abs video">
  <svg width="66" height="66" viewBox="0 0 66 66" aria-label="Play video">
    <circle cx="33" cy="33" r="30" fill="none" stroke="#fff" stroke-width="4"/>
    <path d="M28 25 L41 33 L28 41 Z" fill="#fff"/>
  </svg>
</div>

<div class="abs form-row" style="top:356px"><label>First Name *</label><span></span></div>
<div class="abs form-row" style="top:380px"><label>Last Name *</label><span></span></div>
<div class="abs form-row" style="top:404px"><label>Email *</label><span></span></div>
<div class="abs privacy">We value your privacy and will not share your info.</div>
<svg class="abs form-arrow" width="62" height="70" viewBox="0 0 62 70" aria-hidden="true">
  <path d="M8 4 Q2 40 40 52" stroke="#6e9fd6" stroke-width="9" fill="none" stroke-linecap="round"/>
  <path d="M36 40 L58 54 L34 66 Z" fill="#6e9fd6"/>
</svg>
<div class="abs btn form-btn">Get FREE Calmridgeway</div>

<h2 class="abs section-title relief-title">Looking for relief from panic and anxiety?</h2>

<section class="abs feature" style="left:153px;top:527px">
  <div class="icon"><svg width="30" height="26" viewBox="0 0 30 26"><rect x="2" y="2" width="26" height="17" fill="none" stroke="#fff" stroke-width="2"/><path d="M5 12 H10 L12 7 L15 16 L18 9 L20 12 H25" stroke="#fff" stroke-width="1.6" fill="none"/><path d="M11 24 H19 M15 19 V24" stroke="#fff" stroke-width="2"/></svg></div>
  <h3>Webinars</h3>
  <p>So go on, take the time to read it. It will help you zero in on the key things or "BIG ROCKS" you need to focus on… <a href="#">read more</a></p>
</section>
<section class="abs feature" style="left:312px;top:527px">
  <div class="icon"><svg width="30" height="26" viewBox="0 0 30 26"><path d="M3 3 H18 V13 H9 L5 17 V13 H3 Z" fill="#fff"/><path d="M21 9 H27 V19 H25 V23 L21 19 H12 V16 H21 Z" fill="#fff"/></svg></div>
  <h3>FREE Calmridgeway</h3>
  <p>So go on, take the time to read it. It will help you zero in on the key things or "BIG ROCKS" you need to focus on… <a href="#">read more</a></p>
</section>
<section class="abs feature" style="left:468px;top:527px">
  <div class="icon"><svg width="26" height="28" viewBox="0 0 26 28"><path d="M8 2 H18 V13 H25 L13 26 L1 13 H8 Z" fill="#fff"/></svg></div>
  <h3>Free Downloads</h3>
  <ul><li>174 Greatest Ads Ever</li><li>367 Greatest headline Ever</li><li>Headline creator Pro</li><li>Swipe File</li></ul>
</section>

<section class="abs about">
  <h2>About Us</h2>
  <div class="abs about-image" role="img" aria-label="About us image"></div>
  <div class="abs about-text">
    <p>Lorem Ipsum is simply dummy text of the printing and typesetting industry. Lorem Ipsum has been the industry's standard dummy text ever since the 1500s, when an unknown printer took a galley of type and scrambled it to make a type specimen book. It has survived not only five centuries, but also the leap into electronic typesetting, remaining essentially unchanged.</p>
    <p>It was popularised in the 1960s with the release of Typeleaf sheets containing Lorem Ipsum passages, and more recently with desktop publishing software like Quillset Layout including versions of Lorem Ipsum.</p>
  </div>
</section>

<div class="abs divider"></div>

<h2 class="abs col-title" style="left:152px;top:852px;width:235px">What’s our secret?</h2>
<p class="abs pill pill-teal" style="top:889px">We’ve both mastered the art of crafting compelling words that sell… better known as copywriting.</p>
<p class="abs pill pill-pale" style="top:924px">Needless to say we work with business owners of all shapes and sizes every day of the week planning their marketing and writing their winning, cash spurting promotions.</p>
<p class="abs pill pill-teal" style="top:958px">We see a lot of copy… and we see the mistakes that get made… errors that keep a business’ marketing grounded like a jumbo jet with one working engine.</p>
<p class="abs secret-report">So to help you we put together a special FREE report The 7 Fatal Errors Many Business Owners Make that Keep their Marketing Grounded Like a One-Engined Jumbo Jet available on this website.</p>
<a class="abs read-more" href="#" style="left:165px;top:1041px">Read more</a>

<h2 class="abs col-title" style="left:395px;top:852px;width:232px">Testimoniales</h2>
<div class="abs avatar" style="left:403px;top:884px;background:radial-gradient(circle at 50% 45%,#d9b59c,#8fa6b8)" role="img" aria-label="Portrait of a smiling man"></div>
<p class="abs quote" style="top:890px">We’ve both mastered the art of crafting compelling words that sell… better known as copywriting..<b>Evan Lowe<br>USA</b></p>
<div class="abs avatar" style="left:403px;top:952px;background:radial-gradient(circle at 50% 45%,#e8c7aa,#b89a72)" role="img" aria-label="Portrait of a smiling woman"></div>
<p class="abs quote" style="top:959px">We’ve both mastered the art of crafting compelling words that sell… better known as copywriting..<b>Evan Lowe<br>USA</b></p>
<a class="abs read-more" href="#" style="left:474px;top:1037px">Read more</a>

<div class="abs cta-bar"><p>Looking for relief from panic and anxiety.</p><span class="btn">Get FREE CALMRIDGEWAY Now!</span></div>

<footer class="abs footer">
  <div class="social"><span></span><span></span><span></span><span></span><span></span><span></span></div>
  <div class="abs footer-links">Privacy Policy &nbsp;·&nbsp; Refund Policy &nbsp;·&nbsp; Terms of Service</div>
  <div class="brand">CALMRIDGEWAY</div>
  <div class="abs copyright">Copyright © 2014</div>
</footer>

</body>
</html>
```